Modern Business Card For A Digital Advertising Company

I'll be print on the Tarn Prints Velour paper http://us.tarnprints.example/products/velour/business-cards.html
Need's to be modern and use the color palette of the logo or gray scales. I think integrating the pixelation of the logo in to the card and having it wrap from one side to the other could be interesting. My company provides ad operations, web development, and number of other services to websites around the world. You can see my website at http://www.pixelharbor.example
Contact info on the card needs to have
Dana Welloby
President
p.555.318.4406
dana@pixelharbor.example
http://www.pixelharbor.example
Doesn't necessarily need to be in that order
Target Market(s)
Website owners
Industry/Entity Type
Business
Look and feel

```html
<!DOCTYPE html>
<html lang="en">
<head>
<meta charset="utf-8">
<title>Pixel Harbor – Business Card</title>
<link rel="stylesheet" href="https://fonts.googleapis.com/css2?family=Roboto:wght@400;500;700&display=swap">
<style>
  :root {
    --canvas: #ececea;
    --card-white: #f6f6f6;
    --green: #7db63a;
    --green-deep: #6aa22c;
    --green-light: #98c95e;
    --ink: #2b2b2b;
    --grey: #6f6f6f;
    --white: #ffffff;
  }
  * { box-sizing: border-box; margin: 0; padding: 0; }
  html, body {
    width: 1200px; height: 1000px; overflow: hidden;
    background: var(--canvas);
    font-family: "Roboto", Arial, sans-serif;
  }
  .sheet {
    position: relative; width: 1200px; height: 1000px;
    display: flex; flex-direction: column; align-items: center; justify-content: center; gap: 60px;
  }
  .card {
    position: relative; width: 700px; height: 400px;
    box-shadow: 0 6px 18px rgba(0,0,0,0.18);
    overflow: hidden;
  }
  /* Front */
  .card--front {
    background: var(--card-white);
    display: flex; flex-direction: column; align-items: center; justify-content: center; gap: 22px;
  }
  .wordmark {
    display: flex; align-items: center; gap: 14px;
    font-weight: 700; letter-spacing: 0.06em; text-transform: uppercase;
  }
  .wordmark__square { width: 34px; height: 34px; background: var(--green); }
  .card--front .wordmark__name { color: var(--green); font-size: 44px; }
  .card--front .site { color: var(--grey); font-size: 20px; letter-spacing: 0.02em; }
  /* Back */
  .card--back {
    background: linear-gradient(160deg, var(--green-light) 0%, var(--green) 45%, var(--green-deep) 100%);
  }
  .card--back .wordmark {
    position: absolute; left: 50px; top: 170px;
  }
  .card--back .wordmark__square { width: 26px; height: 26px; background: var(--white); }
  .card--back .wordmark__name { color: var(--white); font-size: 30px; }
  .divider {
    position: absolute; left: 320px; top: 70px; width: 2px; height: 240px; background: var(--white);
  }
  .contact {
    position: absolute; left: 350px; top: 80px;
    color: var(--white); letter-spacing: 0.14em; line-height: 1.45;
  }
  .contact__name { font-size: 22px; font-weight: 700; }
  .contact__title { font-size: 20px; font-weight: 500; margin-bottom: 14px; }
  .contact__line { font-size: 19px; display: block; }
  .pixel-field {
    position: absolute; right: 40px; bottom: 40px; width: 360px; height: 120px;
    background: linear-gradient(90deg, rgba(255,255,255,0) 0%, rgba(255,255,255,0.18) 100%);
  }
</style>
</head>
<body>
<main class="sheet">
  <section class="card card--front" aria-label="Card front">
    <div class="wordmark">
      <span class="wordmark__square"></span>
      <span class="wordmark__name">Pixel Harbor</span>
    </div>
    <p class="site">www.pixelharbor.example</p>
  </section>

  <section class="card card--back" aria-label="Card back">
    <div class="pixel-field" role="img" aria-label="Scattered pixel square pattern in light green"></div>
    <div class="wordmark">
      <span class="wordmark__square"></span>
      <span class="wordmark__name">Pixel Harbor</span>
    </div>
    <span class="divider"></span>
    <div class="contact">
      <p class="contact__name">Dana Welloby</p>
      <p class="contact__title">President</p>
      <span class="contact__line">555.318.4406</span>
      <span class="contact__line">dana@pixelharbor.example</span>
      <span class="contact__line">www.pixelharbor.example</span>
    </div>
  </section>
</main>
</body>
</html>
```